Meridel Hair Studio Needs a new appointment business card

We need a new appointment card for our hair salon.

I Dont want bright out there colours.
I would like it to be neat, clean, easy to read. White, Black, with a hint of colour if needed.

We need
-Logo
-Phone number 47208613
-Mobile Number: 0417306852
Address: Shop 3/214 Calder Road, The Elmgates, Carrowby 4812

BACK SIDE OF CARD
- Appointment Time & Date (White background so we are able to write on it)
(If you are unable to make your appointment please contact us ASAP 47208613)

I also would like the chatterly and Pictorama logo(Find us on Chatterly)(find us on Pictorama)

Target Market(s)

appointment card simple to read. all information for their next appoint For all our clients male and female

Industry/Entity Type

Hairdresser

Contact Information for Business Card

-Logo
-Phone number 47208613

BACK SIDE OF CARD

Font styles to use
Serif
Sans Serif
Script

Requirements
Must have
• White Back ground on backside with appointment deatils so we are able to write information (like appointment time and date)
Nice to have
• Find us on Chatterly
and
pictorama - meridel_hairstudio
Should not have
• BRIGHT COLOURS

```html
<!DOCTYPE html>
<html lang="en">
<head>
<meta charset="utf-8">
<title>Meridel Hair Studio – Appointment Card</title>
<link href="https://fonts.googleapis.com/css2?family=Arimo:wght@400&family=Roboto+Slab:wght@300;400&display=swap" rel="stylesheet">
<style>
  :root {
    --backdrop: #d3d4d7;
    --card-dark: #231f20;
    --card-light: #ffffff;
    --ink-light: #ffffff;
    --ink-dark: #2b2b2b;
    --rule-dark: #3a3a3a;
    --edge: #8a8a8a;
    --social-a: #3f5a9c;
    --social-b: #b0476f;
  }
  * { margin: 0; padding: 0; box-sizing: border-box; }
  html, body {
    width: 1200px; height: 1200px; overflow: hidden;
    background: var(--backdrop);
  }
  .canvas { position: relative; width: 1200px; height: 1200px; }

  .card {
    position: absolute; top: 250px; width: 400px; height: 700px;
    border-radius: 18px; overflow: hidden;
  }
  .card--front { left: 180px; background: var(--card-dark); color: var(--ink-light); }
  .card--back { left: 620px; background: var(--card-light); color: var(--ink-dark); border: 1px solid var(--edge); }

  /* Front */
  .brand { position: absolute; top: 188px; left: 0; width: 100%; text-align: center; }
  .brand__name {
    font-family: "Roboto Slab", serif; font-weight: 400;
    font-size: 46px; letter-spacing: 1px; line-height: 1;
  }
  .brand__tag {
    font-family: "Arimo", sans-serif; font-size: 15px;
    letter-spacing: 0.5px; margin-top: 8px;
  }
  .phones {
    position: absolute; top: 376px; left: 0; width: 100%; text-align: center;
    font-family: "Arimo", sans-serif; font-size: 24px; line-height: 32px;
  }
  .divider { position: absolute; top: 444px; left: 38px; width: 324px; height: 36px; }
  .address {
    position: absolute; top: 489px; left: 0; width: 100%; text-align: center;
    font-family: "Roboto Slab", serif; font-weight: 300; font-size: 23px; line-height: 28px;
    letter-spacing: 0.4px;
  }

  /* Back */
  .appt__title {
    position: absolute; top: 274px; left: 41px; width: 320px;
    font-family: "Roboto Slab", serif; font-weight: 300; font-size: 20px; letter-spacing: 0.6px;
    white-space: nowrap;
  }
  .field {
    position: absolute; left: 55px; width: 300px; height: 24px;
    font-family: "Arimo", sans-serif; font-size: 16px;
  }
  .field--date { top: 357px; }
  .field--time { top: 405px; }
  .field__label { position: absolute; left: 0; top: 0; }
  .field__line { position: absolute; top: 15px; width: 155px; border-top: 1px solid var(--rule-dark); }
  .field--date .field__line { left: 80px; }
  .field--time .field__line { left: 78px; }
  .field__unit { position: absolute; left: 244px; top: 5px; font-size: 11px; }

  .socials {
    position: absolute; top: 598px; left: 0; width: 100%;
    display: flex; justify-content: center; gap: 26px;
    font-family: "Arimo", sans-serif; font-size: 15px; color: var(--ink-dark);
  }
  .social { display: flex; align-items: center; gap: 7px; }
  .social__dot { width: 30px; height: 30px; border-radius: 50%; }
  .social--chatterly .social__dot { background: var(--social-a); }
  .social--pictorama .social__dot { background: var(--social-b); }
</style>
</head>
<body>
<main class="canvas">
  <section class="card card--front" aria-label="Card front">
    <div class="brand">
      <div class="brand__name">MERIDEL</div>
      <div class="brand__tag">HAIR-STUDIO</div>
    </div>
    <div class="phones">
      <div class="phones__landline">47208613</div>
      <div class="phones__mobile">0417306852</div>
    </div>
    <svg class="divider" viewBox="0 0 324 36" aria-hidden="true">
      <line x1="0" y1="18" x2="122" y2="18" stroke="#fff" stroke-width="1.2"/>
      <line x1="202" y1="18" x2="324" y2="18" stroke="#fff" stroke-width="1.2"/>
      <path d="M137 8 l5 -2 l3 6 l-3 2 q1 5 6 9 l2 -2 l5 4 l-2 4 q-12 -2 -16 -21z" fill="#fff"/>
      <rect x="165" y="5" width="12" height="24" rx="2" fill="none" stroke="#fff" stroke-width="2.2"/>
      <line x1="169" y1="25" x2="173" y2="25" stroke="#fff" stroke-width="1.5"/>
    </svg>
    <div class="address">
      <div>Shop 3/214 Calder Road,</div>
      <div>The Elmgates, Carrowby 4812</div>
    </div>
  </section>

  <section class="card card--back" aria-label="Card back">
    <h2 class="appt__title">YOUR NEXT APPOINTMENT IS</h2>
    <div class="field field--date">
      <span class="field__label">DATE:</span>
      <span class="field__line"></span>
    </div>
    <div class="field field--time">
      <span class="field__label">TIME:</span>
      <span class="field__line"></span>
      <span class="field__unit">AM/PM</span>
    </div>
    <div class="socials">
      <div class="social social--chatterly"><span class="social__dot"></span>Chatterly</div>
      <div class="social social--pictorama"><span class="social__dot"></span>Pictorama</div>
    </div>
  </section>
</main>
</body>
</html>
```